fizzy drinks label design

I want to design fizzy drink label for 3 flavors : black grapes, red apple and mojito, band name kestrova, product name TOLMA , product will be in plastic bottle, label size 198 mm X 66mm

```html
<!DOCTYPE html>
<html lang="en">
<head>
<meta charset="utf-8">
<title>TOLMA fizzy drink labels</title>
<link rel="stylesheet" href="https://fonts.googleapis.com/css2?family=Fredoka:wght@500;600;700&family=Roboto+Condensed:wght@500;700&display=swap">
<style>
  :root {
    --bg-top: #f2f2f2;
    --bg-mid: #8c8c8c;
    --bg-bottom: #262626;
    --brand-red: #d8232a;
    --band-red: #b3121f;
    --white: #ffffff;
    --grape-bg: #9b5fae;
    --grape-dot: #6b3b80;
    --grape-title: #f06aa8;
    --lime-bg: #ecea1c;
    --lime-dot: #b9d634;
    --lime-title: #2f7a1c;
    --apple-bg: #f1c21c;
    --apple-dot: #52a22c;
    --apple-title: #e4202b;
    --vit-green: #2f7a1c;
    --vit-orange: #f39a1e;
  }
  * { box-sizing: border-box; margin: 0; padding: 0; }
  html, body { width: 1200px; height: 878px; overflow: hidden; }
  body {
    background: linear-gradient(180deg, var(--bg-top) 0%, var(--bg-mid) 45%, var(--bg-bottom) 100%);
    font-family: "Fredoka", sans-serif;
  }
  .label-stack {
    position: absolute;
    top: 39px; left: 240px;
    display: flex; flex-direction: column; gap: 40px;
  }
  .label {
    position: relative;
    width: 720px; height: 240px;
    overflow: hidden;
    box-shadow: 0 8px 24px rgba(0,0,0,.35);
  }
  .label--grape { background: linear-gradient(90deg, #b07cc0, var(--grape-bg) 50%, #a36ab5); }
  .label--mojito { background: var(--lime-bg); }
  .label--apple { background: var(--apple-bg); }

  .label__dots { position: absolute; inset: 0; }

  .label__brand {
    position: absolute; top: 10px; left: 0; width: 100%;
    text-align: center;
    font-weight: 700; font-size: 42px; letter-spacing: 1px; line-height: 1;
    color: var(--brand-red);
  }
  .label__flavour {
    position: absolute; top: 56px; left: 0; width: 100%;
    text-align: center;
    font-weight: 600; font-size: 34px; letter-spacing: -0.5px; line-height: 1;
  }
  .label--grape .label__flavour { color: var(--grape-title); }
  .label--mojito .label__flavour { color: var(--lime-title); }
  .label--apple .label__flavour { color: var(--apple-title); }

  .label__art {
    position: absolute; top: 98px; left: 290px;
    width: 140px; height: 100px; border-radius: 24px;
  }
  .label--grape .label__art { background: radial-gradient(circle, #4b2a86, #8a3b9e 65%, #b763b6); }
  .label--mojito .label__art { background: radial-gradient(circle, #e3f28a, #9ad23e 70%, #6fae2e); }
  .label--apple .label__art { background: radial-gradient(circle, #e5242e, #c61b24 60%, #6fb33a); }

  .vitamin {
    position: absolute; top: 112px; left: 222px;
    display: flex; flex-direction: column; align-items: flex-start;
  }
  .vitamin__b {
    width: 16px; height: 16px; border-radius: 50%;
    background: var(--vit-green); color: var(--white);
    font-size: 10px; font-weight: 600; text-align: center; line-height: 16px;
  }
  .vitamin__c {
    margin: -6px 0 0 10px;
    width: 28px; height: 28px; border-radius: 50%;
    background: var(--vit-orange); color: var(--white);
    font-size: 17px; font-weight: 700; text-align: center; line-height: 25px;
    border: 2px solid var(--white);
  }
  .vitamin__text {
    margin-top: 2px;
    font-family: "Roboto Condensed", sans-serif;
    font-size: 8px; color: var(--brand-red); line-height: 1.15;
  }
  .vitamin__sub { font-size: 6px; color: #3a3a3a; }

  .label__band {
    position: absolute; left: 0; bottom: 0;
    width: 100%; height: 36px;
    background: linear-gradient(180deg, #c61b26, var(--band-red));
  }
  .label__net {
    position: absolute; left: 222px; bottom: 12px;
    font-family: "Roboto Condensed", sans-serif;
    font-weight: 700; font-size: 11px; color: var(--white);
  }
  .maker {
    position: absolute; left: 440px; bottom: 4px;
    width: 64px; height: 64px; border-radius: 50%;
    background: var(--band-red);
    display: flex; flex-direction: column; align-items: center; justify-content: center;
    color: var(--white);
  }
  .maker__by { font-size: 9px; font-weight: 500; line-height: 1; }
  .maker__name { font-size: 13px; font-weight: 600; line-height: 1.1; }
</style>
</head>
<body>
<main class="label-stack">

  <section class="label label--grape">
    <svg class="label__dots" width="720" height="240" aria-hidden="true">
      <circle cx="250" cy="70" r="9" fill="var(--grape-dot)"/>
      <circle cx="470" cy="108" r="18" fill="#5a2a6e"/>
      <circle cx="478" cy="160" r="9" fill="#7e4a92"/>
      <circle cx="262" cy="100" r="5" fill="#c79ad3"/>
    </svg>
    <div class="label__brand">TOLMA</div>
    <h2 class="label__flavour">Black Grapes</h2>
    <div class="label__art" role="img" aria-label="Illustration of a bunch of black grapes with leaves and a juice splash"></div>
    <div class="vitamin">
      <span class="vitamin__b">B</span>
      <span class="vitamin__c">C</span>
      <span class="vitamin__text">Vitamin C<br><span class="vitamin__sub">(Ascorbic acid)</span></span>
    </div>
    <div class="label__band"></div>
    <p class="label__net">Net Content 200ml Approx.</p>
    <div class="maker"><span class="maker__by">by</span><span class="maker__name">kestrova</span></div>
  </section>

  <section class="label label--mojito">
    <svg class="label__dots" width="720" height="240" aria-hidden="true">
      <circle cx="250" cy="70" r="9" fill="var(--lime-dot)"/>
      <circle cx="470" cy="108" r="18" fill="var(--lime-dot)"/>
      <circle cx="478" cy="160" r="7" fill="#9ac235"/>
      <circle cx="262" cy="100" r="5" fill="#c6dc3a"/>
    </svg>
    <div class="label__brand">TOLMA</div>
    <h2 class="label__flavour">Mojito</h2>
    <div class="label__art" role="img" aria-label="Illustration of lime slices and mint leaves with a juice splash"></div>
    <div class="vitamin">
      <span class="vitamin__b">B</span>
      <span class="vitamin__c">C</span>
      <span class="vitamin__text">Vitamin C<br><span class="vitamin__sub">(Ascorbic acid)</span></span>
    </div>
    <div class="label__band"></div>
    <p class="label__net">Net Content 200ml Approx.</p>
    <div class="maker"><span class="maker__by">by</span><span class="maker__name">kestrova</span></div>
  </section>

  <section class="label label--apple">
    <svg class="label__dots" width="720" height="240" aria-hidden="true">
      <circle cx="250" cy="70" r="9" fill="var(--apple-dot)"/>
      <circle cx="470" cy="108" r="18" fill="#3f8f2a"/>
      <circle cx="478" cy="160" r="7" fill="#3f8f2a"/>
      <circle cx="262" cy="100" r="5" fill="#e6d22c"/>
    </svg>
    <div class="label__brand">TOLMA</div>
    <h2 class="label__flavour">Red Apple</h2>
    <div class="label__art" role="img" aria-label="Illustration of a red apple and an apple slice with a juice splash"></div>
    <div class="vitamin">
      <span class="vitamin__b">B</span>
      <span class="vitamin__c">C</span>
      <span class="vitamin__text">Vitamin C<br><span class="vitamin__sub">(Ascorbic acid)</span></span>
    </div>
    <div class="label__band"></div>
    <p class="label__net">Net Content 200ml Approx.</p>
    <div class="maker"><span class="maker__by">by</span><span class="maker__name">kestrova</span></div>
  </section>

</main>
</body>
</html>
```